Cedar nest sal
Affordable luxury
Professional
Paul dorsey
Doesn't matter, just write anything, will finalize later
Pauldorsey@quillmarsh.net
All I need is a template that suits the logo, I expect a draft template from your side.
It should include, the name, title, company logo, subtitle, website address, physical address, phone number and email. Thank you
Please suggest
Design number 1 will be used
red as second option

```html
<!DOCTYPE html>
<html lang="en">
<head>
<meta charset="utf-8">
<title>Cedar Nest Sal – Business Card</title>
<link rel="stylesheet" href="https://fonts.googleapis.com/css2?family=PT+Sans:ital,wght@0,400;1,700&family=PT+Serif:wght@400&display=swap">
<style>
  :root {
    --backdrop: #2b2b2b;
    --card: #ffffff;
    --leaf: #5e962c;
    --leaf-dark: #4c7f20;
    --bark: #5a3614;
    --ink: #222222;
    --name-ink: #ffffff;
  }
  html, body {
    margin: 0;
    padding: 0;
    width: 1200px;
    height: 780px;
    overflow: hidden;
    background: var(--backdrop);
  }
  .canvas {
    position: relative;
    width: 1200px;
    height: 780px;
  }
  .card {
    position: absolute;
    left: 100px;
    top: 105px;
    width: 1000px;
    height: 570px;
    background: var(--card);
    border-radius: 34px;
    overflow: hidden;
    box-shadow: 0 10px 30px rgba(0,0,0,0.45);
  }
  .card-band {
    position: absolute;
    inset: 0;
    width: 1000px;
    height: 570px;
  }
  .holder {
    position: absolute;
    right: 48px;
    top: 40px;
    text-align: right;
    color: var(--name-ink);
    font-family: "PT Sans", sans-serif;
  }
  .holder-name {
    font-style: italic;
    font-weight: 700;
    font-size: 34px;
    line-height: 1.1;
  }
  .holder-title {
    font-size: 27px;
    line-height: 1.2;
  }
  .brand {
    position: absolute;
    left: 70px;
    top: 300px;
    display: flex;
    align-items: center;
    gap: 16px;
  }
  .brand-mark {
    width: 30px;
    height: 30px;
    background: var(--leaf);
  }
  .brand-name {
    font-family: "PT Serif", serif;
    font-size: 52px;
    color: var(--bark);
    white-space: nowrap;
  }
  .address {
    position: absolute;
    right: 42px;
    top: 296px;
    text-align: right;
    font-family: "PT Serif", serif;
    font-size: 24px;
    line-height: 1.3;
    color: var(--ink);
  }
  .phones {
    position: absolute;
    right: 42px;
    top: 384px;
    display: flex;
    gap: 18px;
    font-family: "PT Serif", serif;
    font-size: 24px;
    color: var(--ink);
  }
  .contact-line {
    display: flex;
    align-items: center;
    gap: 7px;
  }
  .icon {
    width: 20px;
    height: 20px;
    fill: var(--leaf);
    flex: none;
  }
  .online {
    position: absolute;
    right: 42px;
    top: 480px;
    display: flex;
    gap: 24px;
    font-family: "PT Serif", serif;
    font-size: 24px;
    color: var(--ink);
  }
</style>
</head>
<body>
<div class="canvas">
  <div class="card">
    <svg class="card-band" viewBox="0 0 1000 570" aria-hidden="true">
      <path d="M0 0 H1000 V150 C760 160 420 210 0 232 Z" fill="var(--leaf)"/>
      <path d="M0 232 C420 210 760 160 1000 150 L1000 156 C760 170 420 230 0 262 Z" fill="var(--bark)"/>
    </svg>

    <div class="holder">
      <div class="holder-name">Paul dorsey</div>
      <div class="holder-title">job title</div>
    </div>

    <div class="brand">
      <span class="brand-mark"></span>
      <span class="brand-name">Cedar Nest Sal</span>
    </div>

    <div class="address">
      Suite 102 Street name<br>
      ,State, Zip 2034,Country
    </div>

    <div class="phones">
      <span class="contact-line">
        <svg class="icon" viewBox="0 0 24 24"><path d="M6.6 10.8a15.1 15.1 0 0 0 6.6 6.6l2.2-2.2a1 1 0 0 1 1-.25 11.4 11.4 0 0 0 3.6.57 1 1 0 0 1 1 1V20a1 1 0 0 1-1 1A17 17 0 0 1 3 4a1 1 0 0 1 1-1h3.5a1 1 0 0 1 1 1c0 1.25.2 2.45.57 3.57a1 1 0 0 1-.25 1z"/></svg>
        555 210 4837
      </span>
      <span class="contact-line">
        <svg class="icon" viewBox="0 0 24 24"><path d="M6 3h12v5H6z M4 9h16a1 1 0 0 1 1 1v8h-3v3H6v-3H3v-8a1 1 0 0 1 1-1z M8 15v4h8v-4z"/></svg>
        555 614 2093
      </span>
    </div>

    <div class="online">
      <span class="contact-line">
        <svg class="icon" viewBox="0 0 24 24"><path d="M12 2a10 10 0 1 0 5 18.7l-1-1.7A8 8 0 1 1 20 12v1.2a1.8 1.8 0 0 1-3.6 0V8h-2v1a5 5 0 1 0 .6 6.6 3.8 3.8 0 0 0 7-2.4V12A10 10 0 0 0 12 2zm0 13a3 3 0 1 1 0-6 3 3 0 0 1 0 6z"/></svg>
        Pauldorsey@quillmarsh.net
      </span>
      <span class="contact-line">
        <svg class="icon" viewBox="0 0 24 24"><path d="M12 2a10 10 0 1 0 0 20 10 10 0 0 0 0-20zm6.9 6h-3a15.6 15.6 0 0 0-1.4-3.6A8 8 0 0 1 18.9 8zM12 4a14 14 0 0 1 1.9 4h-3.8A14 14 0 0 1 12 4zM4.3 14a8 8 0 0 1 0-4h3.4a16 16 0 0 0 0 4zm.8 2h3a15.6 15.6 0 0 0 1.4 3.6A8 8 0 0 1 5.1 16zm3-8h-3a8 8 0 0 1 4.4-3.6A15.6 15.6 0 0 0 8.1 8zM12 20a14 14 0 0 1-1.9-4h3.8A14 14 0 0 1 12 20zm2.3-6H9.7a14 14 0 0 1 0-4h4.6a14 14 0 0 1 0 4zm.2 5.6a15.6 15.6 0 0 0 1.4-3.6h3a8 8 0 0 1-4.4 3.6zm1.8-5.6a16 16 0 0 0 0-4h3.4a8 8 0 0 1 0 4z"/></svg>
        www.cedarnestsal.com
      </span>
    </div>
  </div>
</div>
</body>
</html>
```